Signage. Will be for store front. Building is on a corner lot. Lots of traffic.

Opening a new location for our landscape business with a garden store (boutique theme) which will have big pottery pots, house plants, ferns and orchids for sale.

And on the side lot of the store we will have bigger bulk items(contractors theme) landscape plants, sod, mulch, soil, rock for sale.

Sign is about 8’x6’

Target Market(s)

Home owners
Landscapers
Builders

Industry/Entity Type

Landscaping

Font styles to use
Sans Serif

Colors
9bcb3c

Requirements
Must have
• “ Installation and Delivery” is a big deal to let people know we do that
Nice to have
• Added a first rendition idea but don’t love it
Added a file with some words to play with
Need help with the words
Should not have
• ?

```html
<!DOCTYPE html>
<html lang="en">
<head>
<meta charset="utf-8">
<title>Verdant Yard Co. – Storefront Sign</title>
<link rel="stylesheet" href="https://fonts.googleapis.com/css2?family=Roboto+Condensed:wght@700&display=swap">
<style>
  :root {
    --canvas-bg: #eef0ea;
    --frame: #3a3a36;
    --sign-white: #ffffff;
    --brand-green: #9bcb3c;
    --band-green: #2f8a2a;
    --band-green-dark: #1f6b22;
    --swoosh-light: #7cc243;
    --name-green: #3f8a2c;
    --bar-yellow: #f2c81e;
    --bar-text: #1e6b1f;
    --text-light: #ffffff;
  }
  * { box-sizing: border-box; margin: 0; padding: 0; }
  html, body {
    width: 900px;
    height: 1200px;
    overflow: hidden;
    background: var(--canvas-bg);
  }
  .sign {
    position: absolute;
    left: 30px;
    top: 200px;
    width: 840px;
    height: 780px;
    border: 14px solid var(--frame);
    background: var(--sign-white);
    box-shadow: 0 8px 24px rgba(0,0,0,0.25);
    overflow: hidden;
  }
  .sign-art {
    position: absolute;
    inset: 0;
    width: 100%;
    height: 100%;
  }
  .brand {
    position: absolute;
    top: 52px;
    right: 44px;
    display: flex;
    align-items: center;
    gap: 18px;
  }
  .brand-name {
    font-family: "Roboto Condensed", sans-serif;
    font-weight: 700;
    font-size: 48px;
    line-height: 1.02;
    letter-spacing: 1px;
    text-transform: uppercase;
    color: var(--name-green);
    text-align: right;
  }
  .brand-dot {
    width: 46px;
    height: 46px;
    border-radius: 50%;
    background: var(--brand-green);
    flex: none;
  }
  .services {
    position: absolute;
    right: 30px;
    top: 484px;
    list-style: none;
    text-align: right;
    font-family: "Roboto Condensed", sans-serif;
    font-weight: 700;
    font-size: 29px;
    line-height: 51px;
    text-transform: uppercase;
    color: var(--text-light);
  }
  .cta-bar {
    position: absolute;
    left: 0;
    right: 0;
    bottom: 0;
    height: 62px;
    background: var(--bar-yellow);
    display: flex;
    align-items: center;
    justify-content: center;
    font-family: "Roboto Condensed", sans-serif;
    font-weight: 700;
    font-size: 36px;
    color: var(--bar-text);
    text-transform: uppercase;
    letter-spacing: 0.5px;
  }
</style>
</head>
<body>
  <div class="sign">
    <svg class="sign-art" viewBox="0 0 812 752" preserveAspectRatio="none" aria-hidden="false">
      <defs>
        <linearGradient id="photoTone" x1="0" y1="0" x2="0.6" y2="1">
          <stop offset="0" stop-color="#3c5a2c"/>
          <stop offset="0.35" stop-color="#8a3a2a"/>
          <stop offset="0.55" stop-color="#4f9a2c"/>
          <stop offset="1" stop-color="#6cbf3a"/>
        </linearGradient>
      </defs>
      <rect class="project-photo" x="0" y="0" width="812" height="700" fill="url(#photoTone)" role="img" aria-label="Photo of a freshly sodded front lawn and house with the company work truck parked beside it"/>
      <path class="header-panel" d="M170,0 H812 V320 C740,225 560,205 400,205 C270,205 190,150 170,0 Z" fill="var(--sign-white)"/>
      <path class="swoosh-light" d="M0,560 C140,600 260,520 390,440 C520,370 650,380 812,350 V390 C650,410 520,410 400,475 C270,545 140,620 0,600 Z" fill="var(--swoosh-light)"/>
      <path class="service-band" d="M0,600 C140,620 270,545 400,475 C520,410 650,410 812,390 V700 H0 Z" fill="var(--band-green)"/>
      <path class="service-band-shade" d="M0,640 C200,660 420,620 812,600 V700 H0 Z" fill="var(--band-green-dark)" opacity="0.35"/>
    </svg>

    <div class="brand">
      <div class="brand-name">Verdant<br>Yard Co.</div>
      <div class="brand-dot"></div>
    </div>

    <ul class="services">
      <li>Landscape</li>
      <li>Garden Supplies</li>
      <li>All Varieties of Plants and Pots</li>
      <li>Removal and Maintenance - Nursery - Sod</li>
    </ul>

    <div class="cta-bar">(555) 010-0147 - Installation and Delivery</div>
  </div>
</body>
</html>
```